Reputable business cards for Diplom Kauffrau, Privat und Geschäftslich

The business cards should be reputable, valuable and elegant in order to be able to use them for business. The design should also include a sophistication that is conspicuous. This could be a picture, an ornament, a sublime print or a kind of logo of the initials of my name "MD". The font should be clear and legible.
Target Market(s)
Business contacts, friends and acquaintances
Contact Information for Business Card
Diplom-Kauffrau Mirela Donat
Lindenhofweg 7 50931 Kerpen
Mobil +49 171 804 29 57
e-mail mirela.donat@postwerk.de
Colors
Designer to choose colors to be used in the design.
Requirements
Must have
- Clear and easy to read font My name in larger font than the other information Visual conspicuity / specificity
Nice to have
- Different colors
Should not have
- Ornate font, playful

```html
<!DOCTYPE html>
<html lang="de">
<head>
<meta charset="UTF-8">
<title>Mirela Donat – Visitenkarte</title>
<link rel="stylesheet" href="https://fonts.googleapis.com/css2?family=Quicksand:wght@300;400&family=PT+Sans:wght@400&display=swap">
<style>
  :root {
    --backdrop: #2a2d33;
    --card: #0b0b0c;
    --name: #d4d4d4;
    --gold: #b99b5f;
    --text: #e4e4e4;
  }
  * { margin: 0; padding: 0; box-sizing: border-box; }
  html, body { width: 1200px; height: 900px; overflow: hidden; }
  body {
    background: var(--backdrop);
    display: flex;
    align-items: center;
    justify-content: center;
  }
  .business-card {
    position: relative;
    width: 760px;
    height: 470px;
    background: var(--card);
    border-radius: 34px;
  }
  .monogram {
    position: absolute;
    left: 208px;
    top: 92px;
    width: 70px;
    text-align: center;
    font-family: "Quicksand", sans-serif;
    font-weight: 400;
    font-size: 34px;
    color: var(--name);
    letter-spacing: 0.04em;
  }
  .identity {
    position: absolute;
    left: 78px;
    top: 168px;
  }
  .identity-name {
    font-family: "Quicksand", sans-serif;
    font-weight: 300;
    font-size: 50px;
    color: var(--name);
    line-height: 1;
  }
  .identity-title {
    margin-top: 10px;
    font-family: "Quicksand", sans-serif;
    font-weight: 400;
    font-size: 15px;
    letter-spacing: 0.42em;
    color: var(--gold);
  }
  .contact-list {
    position: absolute;
    left: 398px;
    top: 272px;
    list-style: none;
    font-family: "PT Sans", sans-serif;
    font-size: 21px;
    color: var(--text);
    line-height: 1.3;
  }
  .contact-item {
    display: flex;
    align-items: flex-start;
    gap: 16px;
    margin-bottom: 6px;
  }
  .contact-icon {
    flex: none;
    width: 16px;
    height: 18px;
    margin-top: 5px;
    fill: var(--gold);
  }
</style>
</head>
<body>
  <article class="business-card">
    <div class="monogram">MD</div>

    <header class="identity">
      <h1 class="identity-name">Mirela Donat</h1>
      <p class="identity-title">DIPLOM-KAUFFRAU</p>
    </header>

    <ul class="contact-list">
      <li class="contact-item">
        <svg class="contact-icon" viewBox="0 0 16 18" aria-hidden="true">
          <path d="M8 0C4.4 0 1.8 2.7 1.8 6.1 1.8 10.4 8 18 8 18s6.2-7.6 6.2-11.9C14.2 2.7 11.6 0 8 0zm0 8.6a2.5 2.5 0 1 1 0-5 2.5 2.5 0 0 1 0 5z"/>
        </svg>
        <span>Lindenhofweg 7 50931<br>Kerpen</span>
      </li>
      <li class="contact-item">
        <svg class="contact-icon" viewBox="0 0 16 18" aria-hidden="true">
          <path d="M4 0h8a1.6 1.6 0 0 1 1.6 1.6v14.8A1.6 1.6 0 0 1 12 18H4a1.6 1.6 0 0 1-1.6-1.6V1.6A1.6 1.6 0 0 1 4 0zm0.6 2v11.6h6.8V2zM8 14.6a1.1 1.1 0 1 0 0 2.2 1.1 1.1 0 0 0 0-2.2z"/>
        </svg>
        <span>+49 171 804 29 57</span>
      </li>
      <li class="contact-item">
        <svg class="contact-icon" viewBox="0 0 16 18" aria-hidden="true">
          <path d="M0 4h16v11H0zm1.6 1.4L8 10.2l6.4-4.8z"/>
        </svg>
        <span>mirela.donat@postwerk.de</span>
      </li>
    </ul>
  </article>
</body>
</html>
```